ソラベルデ調の24時間ジムです。
グランドオープン4月1日に向けてのチラシ作成依頼です。
24時間ジム月会費:6,500円(税抜)、パーソナルトレーニング月4回30分:16,000円(税抜)、パーソナルストレッチ月4回30分:16,000円(税抜)という3点を記載の上、パーソナルサービスご契約者様はご契約期間中は24時間ジム月会費無料というポイントを強調して下さい。
※パーソナルトレーニングとは、スタッフがお客様の目的を基にトレーニングメニュー作成とトレーニング補助を行います。また、食事等のご相談にもお答えします。
※パーソナルストレッチとは、スタッフがお客様の目的を基に、ストレッチによってお客様の凝りや不調を解消するサービスであり、トレーニング時の可動域増加、トレーニング後のリラックスとして利用頂けます。
ストレッチエリア、フリーウェイト、トレーニングマシン、有酸素マシンを完備している点を記載しても構いません。
空気清浄機を設置して換気は十分に行い、手指消毒、マシン消毒も徹底して行います。
店舗が茅ヶ崎市内にある為、「ミルコ」「海」「湘南」といった言葉を連想しつつも、一般大衆的なチラシの作成をお願いします。
配布も茅ヶ崎市内限定に限らせて頂くので、その点を強調しても構いません。
電話番号:0467-39-2751/住所:253-0086 神奈川県茅ヶ崎市浜見平3丁目2-9ミント・ハイツ中央2F・3F/ロゴ※添付資料としてお送りします。
A4
両面
茶系
• 高解像度JPG (.jpg)
• イラストレーター形式 (.ai)
• フォトショップ形式 (.psd)
• PNG形式 (.png)
以前、プレオープン用に作成したチラシに加えて、弊ジムロゴを添付致します。
どちらもai形式でお渡し可能です。
一点、修正点がございます。

月4回30分のパーソナルサービスを、月2回50分のパーソナルサービスに変更お願い致します。

価格設定は変更ございませんので、よろしくお願い致します。
ロゴ、チラシのaiファイルを添付しますので、ご活用よろしくお願い致します。

https://files.example-drop.test/a1b2c3d4e5

以上のリンク先より、ダウンロードの程、よろしくお願い致します。
申し訳ございません。

先程、追記致しましたパーソナルサービス内容は一旦破棄とさせて頂き、改めてお送り致します。

パーソナルトレーニング、パーソナルストレッチ共に月2回30分15,000円(税抜)、月4回30分22,000円(税抜)の内容となります。

上記内容で修正お願い致します。
https://files.example-drop.test/f6g7h8i9j0

店舗内装、外観を上記リンクにまとめました。

ご活用下さいませ。

内装のウッド調と海っぽさが調和した内容で、24時間ジムであることを謳いつつ、パーソナルサービスも提供していることも強調出来ていたので、選びました。

皆さま、短い期間で質の高いデザインを作成頂き、ありがとうございました。
今後も、チラシを作成する機会にございましたら、何卒宜しくお願い致します。

```html
<!DOCTYPE html>
<html lang="ja">
<head>
<meta charset="utf-8">
<title>ハルモア茅ヶ崎24 グランドオープン</title>
<link rel="stylesheet" href="https://fonts.googleapis.com/css2?family=Oswald:wght@600;700&family=Noto+Sans+JP:wght@500;700;900&family=Great+Vibes&display=swap">
<style>
  :root {
    --ink: #1a1a1a;
    --paper: #ffffff;
    --yellow: #f7d417;
    --gold: #b8925a;
    --orange: #f08a1c;
    --sea: #2a7fc1;
    --grey: #6b6b6b;
  }
  * { margin: 0; padding: 0; box-sizing: border-box; }
  html, body { width: 900px; height: 1200px; overflow: hidden; background: var(--paper); }
  .flyer { position: relative; width: 900px; height: 1200px; background: var(--paper); font-family: "Noto Sans JP", sans-serif; color: var(--ink); overflow: hidden; }

  .hero-photo { position: absolute; left: 300px; top: 0; width: 600px; height: 500px;
    background: linear-gradient(160deg, #e9e6e2 0%, #cfc8c0 45%, #8a7f76 75%, #f3f1ee 100%); }
  .hero-fade-left { position: absolute; left: 300px; top: 0; width: 220px; height: 500px;
    background: linear-gradient(90deg, var(--paper), rgba(255,255,255,0)); }
  .hero-fade-bottom { position: absolute; left: 300px; top: 400px; width: 600px; height: 100px;
    background: linear-gradient(180deg, rgba(255,255,255,0), var(--paper)); }

  .headline { position: absolute; left: 62px; top: 50px; font-family: "Oswald", sans-serif; font-weight: 700;
    font-size: 72px; line-height: 0.98; letter-spacing: 1px; color: var(--ink); }

  .hours-badge { position: absolute; left: 262px; top: 170px; width: 124px; height: 124px; border-radius: 50%;
    background: var(--yellow); text-align: center; padding-top: 22px; }
  .hours-badge .big { font-family: "Oswald", sans-serif; font-weight: 700; font-size: 42px; line-height: 1; }
  .hours-badge .small { font-weight: 700; font-size: 14px; line-height: 1.25; margin-top: 4px; }

  .grand-open { position: absolute; left: 70px; top: 300px; font-family: "Great Vibes", cursive;
    font-size: 120px; line-height: 1; color: var(--gold); }

  .date-badge { position: absolute; left: 700px; top: 320px; width: 140px; height: 140px; border-radius: 50%;
    background: var(--yellow); text-align: center; padding-top: 30px; }
  .date-badge .date { font-family: "Oswald", sans-serif; font-weight: 700; font-size: 56px; line-height: 1; }
  .date-badge .day { font-weight: 700; font-size: 17px; }

  .brand { position: absolute; left: 110px; top: 500px; width: 650px; text-align: center;
    font-weight: 900; font-size: 70px; line-height: 1.3; color: var(--ink); letter-spacing: 2px; white-space: nowrap; }
  .brand-waves { position: absolute; left: 776px; top: 524px; width: 86px; height: 50px; background: var(--sea); border-radius: 4px; }

  .services { position: absolute; left: 50px; top: 610px; width: 800px; display: flex; justify-content: space-between; }
  .service { width: 390px; text-align: center; }
  .service .lead { font-weight: 700; font-size: 22px; line-height: 1.3; }
  .service .title { font-weight: 900; font-size: 36px; color: var(--orange); line-height: 1.2; margin-bottom: 10px; }
  .service ul { list-style: none; font-weight: 500; font-size: 17px; line-height: 1.65; white-space: nowrap; }
  .service .price { margin-top: 10px; font-weight: 700; font-size: 15px; line-height: 1.55; white-space: nowrap;
    border-top: 1px solid var(--gold); padding-top: 6px; }

  .free-band { position: absolute; left: 40px; top: 910px; width: 820px; height: 116px; background: var(--ink);
    display: flex; align-items: center; justify-content: space-between; padding: 0 36px; }
  .free-band .target { color: var(--paper); font-weight: 700; font-size: 28px; line-height: 1.3; }
  .free-band .offer { text-align: right; }
  .free-band .regular { color: var(--paper); font-weight: 500; font-size: 15px; }
  .free-band .offer-text { color: var(--yellow); font-weight: 900; font-size: 58px; line-height: 1.1; }

  .footer { position: absolute; left: 40px; top: 1058px; width: 820px; height: 110px; display: flex; align-items: center; gap: 26px; }
  .footer-brand { font-weight: 900; font-size: 28px; line-height: 1.15; width: 170px; }
  .footer-address { font-size: 13px; font-weight: 500; line-height: 1.5; color: var(--grey); width: 230px; }
  .footer-contact { display: flex; flex-direction: column; gap: 6px; }
  .phone { display: flex; align-items: center; gap: 8px; font-family: "Oswald", sans-serif; font-weight: 700; font-size: 42px; }
  .web { font-size: 14px; color: var(--grey); border: 1px solid var(--grey); padding: 2px 10px; align-self: flex-start; }
</style>
</head>
<body>
<div class="flyer">
  <div class="hero-photo" role="img" aria-label="ジム内のラックの前に立つトレーニングウェアの女性の写真"></div>
  <div class="hero-fade-left"></div>
  <div class="hero-fade-bottom"></div>

  <h1 class="headline">24HOUR<br>OPEN<br>GYM</h1>

  <div class="hours-badge">
    <div class="big">24h</div>
    <div class="small">24時間<br>営業</div>
  </div>

  <div class="grand-open">Grand Open</div>

  <div class="date-badge">
    <div class="date">4/1</div>
    <div class="day">木曜</div>
  </div>

  <div class="brand">ハルモア茅ヶ崎24</div>
  <div class="brand-waves" role="img" aria-label="青い波の飾り"></div>

  <section class="services">
    <div class="service">
      <p class="lead">あなただけの</p>
      <h2 class="title">パーソナル<br>トレーニング</h2>
      <ul>
        <li>あなたに最適のトレーニングメニューを作成</li>
        <li>プロのトレーナーの最適な補助で効果アップ</li>
        <li>効果を引き出す食事内容をアドバイス</li>
      </ul>
      <p class="price">月2回30分 15,000円（税抜）<br>月4回30分 22,000円（税抜）</p>
    </div>
    <div class="service">
      <p class="lead">あなただけの</p>
      <h2 class="title">パーソナル<br>ストレッチ</h2>
      <ul>
        <li>凝りや不調を解消します</li>
        <li>身体の柔軟さをアップ</li>
        <li>運動後のリラックス効果</li>
      </ul>
      <p class="price">月2回30分 15,000円（税抜）<br>月4回30分 22,000円（税抜）</p>
    </div>
  </section>

  <div class="free-band">
    <p class="target">パーソナルサービス<br>ご契約者様</p>
    <div class="offer">
      <p class="regular">24時間ジム月会費 6,500円（税抜）が</p>
      <p class="offer-text">月会費無料</p>
    </div>
  </div>

  <footer class="footer">
    <div class="footer-brand">ハルモア<br>茅ヶ崎24</div>
    <p class="footer-address">〒253-0086<br>神奈川県茅ヶ崎市浜見平3丁目2-9<br>ミント・ハイツ中央2F・3F</p>
    <div class="footer-contact">
      <div class="phone">
        <svg width="34" height="34" viewBox="0 0 24 24" aria-hidden="true"><path fill="#1a1a1a" d="M6.6 10.8a15.1 15.1 0 0 0 6.6 6.6l2.2-2.2c.3-.3.7-.4 1-.2 1.1.4 2.3.6 3.6.6.6 0 1 .4 1 1V20c0 .6-.4 1-1 1A17 17 0 0 1 3 4c0-.6.4-1 1-1h3.5c.6 0 1 .4 1 1 0 1.3.2 2.5.6 3.6.1.3 0 .7-.2 1z"/></svg>
        0467-39-2751
      </div>
      <div class="web">www.harumore24.example ｜ ハルモア茅ヶ崎24 検索</div>
    </div>
  </footer>
</div>
</body>
</html>
```